Humorous Book by Comedian Needs E-book Cover

My book 'A Kettle on the Porch' is on Leafpad but I want a better cover designed. Cover needs my photo on it. My name is the most important text (because I have an existing audience.)

Text elements:
Author: Dorvel Pim
Title: A Kettle on the Porch
Subtitle: Tenth Anniversary Edition
Review Quote: 'All of his columns are amusing. The best are masterpieces.' Harbour Ledger

Above my name it should say: Collected Humour From NZ's Award-Winning Comedian

Here's the present version (which is why I want an improved version!)
http://www.brightmart-example.com/A-Kettle-Porch-Anniversary-Edition-ebook/dp/Q77TX2M904

Book covers I admire:

http://www.brightmart-example.co.uk/Why-The-Fern-Odile-Brask-ebook/dp/Q3318ZR7LN/ref=tmm_kin_title_0

http://www.brightmart-example.com/Gravelhat-Mira-Dunst-ebook/dp/Q691PLE583/ref=tmm_kin_title_0

http://www.brightmart-example.co.uk/Why-Keep-Lantern-Rex-Palfrey-ebook/dp/Q58JN3TQ7V

Leafpad covers need to work as thumbnails, as well as on small device screens.

This cover is for Brightmart Leafpad. Tech specs are on Leafpad Direct Publishing page. Dimensions: Requirements for the size of your cover art have an ideal height/width ratio of 1.6, this means: • A minimum of 625 pixels on the shortest side and 1000 pixels on the longest side • For best quality, your image would be 2820 pixels on the shortest side and 4500 pixels on the longest side

Dimensions Requirements for the size of your cover art have an ideal height/width ratio of 1.6, this means: • A minimum of 625 pixels on the shortest side and 1000 pixels on the longest side • For best quality, your image would be 2820 pixels on the shortest side and 4500 pixels on the longest side

Comedian

```html
<!DOCTYPE html>
<html lang="en">
<head>
<meta charset="utf-8">
<title>Dorvel Pim – A Kettle on the Porch</title>
<link rel="stylesheet" href="https://fonts.googleapis.com/css2?family=Bebas+Neue&family=Open+Sans:ital,wght@1,600;1,700&family=Sue+Ellen+Francisco&display=swap">
<style>
  :root {
    --lime: #def31c;
    --lime-deep: #cfe812;
    --band-pink: #ee3f73;
    --jacket-pink: #ec2f6b;
    --jacket-dark: #b81c4e;
    --sky: #3ec3e6;
    --teal: #1d8896;
    --title-teal: #2a92a6;
    --ink: #1f2a1c;
    --white: #ffffff;
  }
  * { margin: 0; padding: 0; box-sizing: border-box; }
  html, body { width: 927px; height: 1200px; overflow: hidden; background: var(--lime); }
  .cover {
    position: relative;
    width: 927px; height: 1200px; overflow: hidden;
    background: radial-gradient(circle at 60% 45%, var(--lime) 0%, var(--lime-deep) 100%);
  }
  .tagline-band {
    position: absolute; left: 0; top: 0; width: 100%; height: 70px;
    background: var(--band-pink);
    display: flex; align-items: center; justify-content: center;
  }
  .tagline {
    font-family: "Open Sans", sans-serif; font-style: italic; font-weight: 600;
    font-size: 31px; color: var(--white); letter-spacing: 0.2px;
  }
  .author {
    position: absolute; left: 102px; top: 62px;
    font-family: "Bebas Neue", sans-serif; font-size: 158px; line-height: 1;
    letter-spacing: 10px; white-space: nowrap;
  }
  .author .first { color: var(--sky); }
  .author .last { color: var(--teal); }
  .edition {
    position: absolute; right: 62px; top: 204px;
    font-family: "Bebas Neue", sans-serif; font-size: 45px; line-height: 1;
    color: var(--white); letter-spacing: 1px;
  }
  .author-photo { position: absolute; left: 0; top: 290px; width: 720px; height: 910px; }
  .title {
    position: absolute; left: 440px; top: 405px; width: 460px;
    font-family: "Sue Ellen Francisco", cursive; font-weight: 400;
    font-size: 118px; line-height: 1.05; color: var(--title-teal);
  }
  .review {
    position: absolute; left: 664px; top: 880px; width: 250px;
    font-family: "Open Sans", sans-serif; font-style: italic; font-weight: 600;
    font-size: 29px; line-height: 41px; color: var(--ink);
  }
  .review cite {
    display: block; margin-top: 8px; font-style: normal; font-weight: 700;
    font-family: "Open Sans", sans-serif; font-size: 23px; letter-spacing: 0.5px;
  }
</style>
</head>
<body>
<main class="cover">
  <header class="tagline-band">
    <p class="tagline">Collected Humour From NZ's Award-Winning Comedian</p>
  </header>

  <h1 class="author"><span class="first">DORVEL</span><span class="last">PIM</span></h1>
  <p class="edition">10TH ANNIVERSARY EDITION</p>

  <svg class="author-photo" viewBox="0 0 720 910" role="img" aria-label="Photo of the author smiling in a bright pink jacket, white shirt and bow tie">
    <defs>
      <linearGradient id="jacket" x1="0" y1="0" x2="0" y2="1">
        <stop offset="0" stop-color="#3a2a25"/>
        <stop offset="0.2" stop-color="#d9a98a"/>
        <stop offset="0.38" stop-color="var(--jacket-pink)"/>
        <stop offset="1" stop-color="var(--jacket-dark)"/>
      </linearGradient>
    </defs>
    <path d="M300 0 C390 0 440 60 440 170 C440 250 420 300 400 330 C520 360 620 420 680 520 C710 600 720 760 720 910 L0 910 L0 420 C60 370 140 340 220 325 C190 290 170 240 170 170 C170 60 220 0 300 0 Z" fill="url(#jacket)"/>
  </svg>

  <h2 class="title">A Kettle On<br>The Porch</h2>

  <blockquote class="review">
    All of his columns are amusing. The best are master-pieces.'
    <cite>.- HARBOUR LEDGER</cite>
  </blockquote>
</main>
</body>
</html>
```